Scrapbooking company Verolumi Facebook

We need a cover design for our Facebook page. We scrap and handmade projects. We would like to convey the idea of ​​creativity, creative workshop (cuts, paintings ...).

Font styles to use
Decorative
Script

```html
<!DOCTYPE html>
<html lang="en">
<head>
<meta charset="utf-8">
<title>Verolumi – Facebook cover options</title>
<link href="https://fonts.googleapis.com/css2?family=Chewy&display=swap" rel="stylesheet">
<style>
  :root {
    --board: #dedede;
    --white: #ffffff;
    --cream: #fdf0d8;
    --brand-red: #e0414d;
    --moon: #f7dc7a;
    --warm-orange: #f5874f;
    --warm-yellow: #fbc93d;
    --soft-pink: #f6b9b4;
    --soft-teal: #9fd3c9;
    --navy: #1c1f40;
    --coral: #ee5360;
    --ring: #fedb91;
    --tool-tone: #e9dcc3;
  }
  * { margin: 0; padding: 0; box-sizing: border-box; }
  html, body { width: 1200px; height: 1200px; overflow: hidden; background: var(--board); }
  .board { position: relative; width: 1200px; height: 1200px; }
  .cover { position: absolute; overflow: hidden; }
  .cover--petals { left: 52px; top: 47px; width: 771px; height: 338px; background: var(--white); }
  .cover--tools { left: 52px; top: 394px; width: 752px; height: 331px; background: var(--cream); }
  .cover--shapes { left: 58px; top: 738px; width: 755px; height: 331px; background: var(--white); }

  .brand {
    position: absolute; display: flex; align-items: center; gap: 12px;
    transform: translate(-50%, -50%); white-space: nowrap;
  }
  .brand__dot { width: 58px; height: 58px; border-radius: 50%; background: var(--moon); flex: none; }
  .brand__name {
    font-family: "Chewy", "Comic Sans MS", cursive;
    font-weight: 400; font-size: 66px; line-height: 1;
    color: var(--brand-red); letter-spacing: 2px;
  }
  .cover--petals .brand { left: 394px; top: 185px; }
  .cover--tools .brand { left: 380px; top: 134px; }
  .cover--tools .brand__name { font-size: 58px; }
  .cover--tools .brand__dot { width: 50px; height: 50px; }
  .cover--shapes .brand { left: 378px; top: 130px; }

  .ornament { position: absolute; }
  .ornament--petals-left {
    left: 0; top: 0; width: 280px; height: 240px;
    background: linear-gradient(135deg, var(--coral), var(--warm-orange) 45%, var(--warm-yellow));
    border-bottom-right-radius: 70% 80%;
    opacity: 0.9;
  }
  .ornament--petals-right {
    right: 0; top: 80px; width: 140px; height: 258px;
    background: linear-gradient(180deg, var(--soft-teal), var(--soft-pink) 55%, #fde7c4);
    border-top-left-radius: 80% 60%;
    opacity: 0.55;
  }

  .tool { position: absolute; background: var(--tool-tone); border-radius: 10px; }
  .tool--tape    { left: 98px;  top: 14px;  width: 50px; height: 50px; border-radius: 50%; }
  .tool--brush   { left: 178px; top: 48px;  width: 120px; height: 14px; border-radius: 7px; transform: rotate(-28deg); }
  .tool--spool   { left: 90px;  top: 116px; width: 58px; height: 36px; }
  .tool--yarn    { left: 192px; top: 194px; width: 40px; height: 40px; border-radius: 50%; }
  .tool--scissors{ left: 104px; top: 200px; width: 64px; height: 82px; border-radius: 40% 40% 30% 30%; }
  .tool--heart   { left: 306px; top: 258px; width: 70px; height: 56px; border-radius: 50% 50% 45% 45%; }
  .tool--pencil  { left: 424px; top: 290px; width: 104px; height: 14px; border-radius: 7px; transform: rotate(28deg); }
  .tool--palette { left: 592px; top: 256px; width: 62px; height: 62px; border-radius: 50% 45% 50% 40%; }
  .tool--jar     { left: 530px; top: 24px;  width: 60px; height: 76px; }
  .tool--needle  { left: 654px; top: 44px;  width: 80px; height: 80px; border-radius: 50% 10% 50% 50%; }
  .tool--tube    { left: 584px; top: 150px; width: 80px; height: 26px; border-radius: 13px; transform: rotate(-38deg); }

  .shapes-layer { position: absolute; inset: 0; }
</style>
</head>
<body>
<main class="board">

  <section class="cover cover--petals" aria-label="Cover option with petal ornaments">
    <div class="ornament ornament--petals-left" role="img" aria-label="Colourful swirling petal ornament in orange, red and yellow"></div>
    <div class="ornament ornament--petals-right" role="img" aria-label="Faded pastel petal ornament"></div>
    <div class="brand">
      <span class="brand__dot"></span>
      <span class="brand__name">Verolumi</span>
    </div>
  </section>

  <section class="cover cover--tools" aria-label="Cover option with craft tool drawings">
    <div class="tool tool--tape" role="img" aria-label="Line drawing of a roll of tape"></div>
    <div class="tool tool--brush" role="img" aria-label="Line drawing of a paintbrush"></div>
    <div class="tool tool--spool" role="img" aria-label="Line drawing of a thread spool"></div>
    <div class="tool tool--scissors" role="img" aria-label="Line drawing of scissors"></div>
    <div class="tool tool--yarn" role="img" aria-label="Line drawing of a yarn ball with knitting needles"></div>
    <div class="tool tool--heart" role="img" aria-label="Line drawing of a stitched heart"></div>
    <div class="tool tool--pencil" role="img" aria-label="Line drawing of a pencil"></div>
    <div class="tool tool--palette" role="img" aria-label="Line drawing of a paint palette"></div>
    <div class="tool tool--jar" role="img" aria-label="Line drawing of a paint jar"></div>
    <div class="tool tool--needle" role="img" aria-label="Line drawing of a threaded needle"></div>
    <div class="tool tool--tube" role="img" aria-label="Line drawing of a glue tube"></div>
    <div class="brand">
      <span class="brand__dot"></span>
      <span class="brand__name">Verolumi</span>
    </div>
  </section>

  <section class="cover cover--shapes" aria-label="Cover option with geometric shapes">
    <svg class="shapes-layer" width="755" height="331" viewBox="0 0 755 331" aria-hidden="true">
      <circle cx="60" cy="63" r="50" fill="none" stroke="var(--coral)" stroke-width="1" stroke-dasharray="4 3"/>
      <circle cx="226" cy="38" r="13" fill="none" stroke="var(--coral)" stroke-width="1.2"/>
      <circle cx="187" cy="113" r="34" fill="none" stroke="var(--ring)" stroke-width="14"/>
      <circle cx="27" cy="263" r="26" fill="none" stroke="var(--ring)" stroke-width="1"/>
      <circle cx="262" cy="330" r="20" fill="none" stroke="var(--coral)" stroke-width="1" stroke-dasharray="3 3"/>
      <circle cx="633" cy="-5" r="60" fill="none" stroke="var(--coral)" stroke-width="1" stroke-dasharray="4 3"/>
      <circle cx="652" cy="43" r="42" fill="var(--soft-teal)"/>
      <circle cx="730" cy="67" r="42" fill="var(--ring)" opacity="0.7"/>
      <polygon points="598,58 612,33 626,58" fill="var(--warm-orange)" opacity="0.75"/>
      <circle cx="715" cy="120" r="50" fill="var(--warm-orange)" opacity="0.5"/>
      <polygon points="540,208 588,125 620,208" fill="var(--coral)" opacity="0.35"/>
      <path d="M600 150 C 600 100, 690 100, 700 130 C 710 170, 660 200, 630 195 C 605 190, 600 175, 600 150 Z" fill="var(--coral)"/>
      <circle cx="710" cy="190" r="38" fill="var(--soft-teal)" opacity="0.6"/>
      <circle cx="715" cy="175" r="15" fill="var(--coral)"/>
      <circle cx="755" cy="185" r="30" fill="var(--coral)"/>
      <path d="M545 331 A 98 98 0 0 1 741 331 Z" fill="var(--navy)"/>
    </svg>
    <div class="brand">
      <span class="brand__dot"></span>
      <span class="brand__name">Verolumi</span>
    </div>
  </section>

</main>
</body>
</html>
```